Website design and Setup for Real Estate Firm and Going Live

We are a commercial real estate investment firm and are looking for a 6 page website which is informational only. Some text and graphics on each page. We would want the designer to code and launch the website. This website needs to be corporate looking as well as innovative. We are setting up the website on webnook.

The first page will be a home page with generic commercial real estate look with a link to the following 5 pages on page 1. So page one (the Home Page should have a commercial real estate look with the text linking to the following pages. Page 2 "About Us" with 3 paragraphs describing our firm. Page 3 "Our Platform" with another few paragraphs on due diligence, acquisitions, financing, and management.

Page 4 is "Our Team" highlighting several manager profiles. Page 5 is our "investment Portfolio portal" which will be password protected so not a lot of text, only general graphics and anyone viewing the site casually won't get into the backend, Page 6 is the contact us page. All of the content will be uploaded shortly.

The project includes setting up hyperlinks in the website as well rotating images etc and a final complete live online product. We do not expect to pay for any stock images.

Target Market(s)

Investors, Real Estate Professionals, Brokerages

Industry/Entity Type

Real Estate

Coding

Coded - Design and coding required

Number of Pages Required

5+ page

Requirements
Must have
• Corporate cutting edge design, suitable for a financial corporation.

```html
<!DOCTYPE html>
<html lang="en">
<head>
<meta charset="utf-8">
<title>Meridian Crest — Real Estate Investment Firm</title>
<link href="https://fonts.googleapis.com/css2?family=Montserrat:wght@300;400;500;600;700;800&display=swap" rel="stylesheet">
<style>
:root{
  --ink:#2b2b2b;
  --text:#444;
  --muted:#7a7a7a;
  --line:#bdbdbd;
  --soft:#efefef;
  --pale:#e8eaeb;
  --grey:#b3b3b3;
  --btn:#8f8f8f;
  --footer:#595959;
  --footer-line:#6d6d6d;
  --white:#fff;
}
*{box-sizing:border-box;margin:0;padding:0}
html,body{width:1200px;height:4065px;overflow:hidden;background:var(--white)}
body{position:relative;font-family:'Montserrat',sans-serif;color:var(--text)}
.abs{position:absolute}
a{color:inherit;text-decoration:none}

/* header */
.site-header{position:absolute;left:0;top:0;width:1200px;height:128px;background:var(--white)}
.brand{position:absolute;left:106px;top:40px;width:210px;text-align:center;font-family:'Montserrat',sans-serif;font-weight:500;font-size:20px;letter-spacing:1px;color:#8a8a8a;text-transform:uppercase}
.call-btn{position:absolute;left:838px;top:0;width:256px;height:41px;background:#8d8d8d;color:var(--white);font-size:13px;font-weight:600;letter-spacing:1px;display:flex;align-items:center;justify-content:center;gap:8px}
.main-nav{position:absolute;top:81px;left:0;font-size:11px;font-weight:600;letter-spacing:.6px;color:var(--muted)}
.main-nav a{position:absolute;white-space:nowrap}
.main-nav a.active{color:var(--ink)}
.nav-underline{position:absolute;left:354px;top:124px;width:108px;height:3px;background:var(--line)}

/* hero */
.hero{position:absolute;left:0;top:128px;width:1200px;height:690px}
.hero-photo{position:absolute;inset:0;background:linear-gradient(180deg,#cfe0ec 0%,#a9c3d6 30%,#6f8ea6 55%,#4a5f5c 75%,#6d6a5e 100%)}
.hero-title{position:absolute;top:122px;width:1200px;text-align:center;font-size:41px;font-weight:300;color:var(--ink);letter-spacing:.5px}
.hero-title b{font-weight:700}
.hero-sub{position:absolute;top:178px;width:1200px;text-align:center;font-size:20px;font-weight:600;letter-spacing:2.5px;color:var(--ink)}
.pill{position:absolute;left:510px;top:219px;width:164px;height:43px;border-radius:22px;background:var(--white);color:#555;font-size:13px;font-weight:600;letter-spacing:1.5px;display:flex;align-items:center;justify-content:center}

/* shared section text */
.eyebrow{position:absolute;font-size:15px;font-weight:400;letter-spacing:2px;color:#555;text-transform:uppercase}
.section-title{position:absolute;font-size:37px;font-weight:300;color:var(--ink);white-space:nowrap}
.section-title b{font-weight:700}
.rule{position:absolute;height:4px;background:var(--line)}
.rule.dark{background:#333}
.copy{position:absolute;font-size:12.5px;line-height:22.5px;color:var(--text);text-align:justify;hyphens:auto;-webkit-hyphens:auto}
.copy p+p{margin-top:14px}
.outline-btn{position:absolute;height:46px;border:2px solid #8c8c8c;color:#666;font-size:13px;font-weight:600;letter-spacing:1.8px;display:flex;align-items:center;justify-content:center}

/* company */
.company-photo{position:absolute;left:142px;top:846px;width:424px;height:396px;border-radius:50% 50% 48% 48%/55% 55% 45% 45%;background:radial-gradient(circle at 50% 40%,#dcebf7 0%,#8fb8dc 45%,#3f6f99 80%,#2e5070 100%)}

/* approach */
.approach{position:absolute;left:0;top:1344px;width:1184px;height:557px;background:var(--soft)}
.card{position:absolute;top:1522px;width:227px;height:248px;color:var(--white);text-align:center}
.card .photo{position:absolute;inset:0}
.card h3{position:absolute;left:0;right:0;top:190px;font-size:14px;font-weight:600;letter-spacing:.3px}
.card p{position:absolute;left:0;right:0;top:214px;font-size:11px;font-weight:400}

/* team */
.team{position:absolute;left:0;top:1901px;width:1200px;height:595px;background:linear-gradient(180deg,#fafafa 0%,#f4f4f4 55%,#d9dadb 100%)}
.team-photo{position:absolute;left:584px;top:16px;width:546px;height:579px;background:linear-gradient(135deg,#c9cbcd 0%,#8d8f92 45%,#a77452 80%,#6e4a35 100%)}

/* portfolio */
.portfolio{position:absolute;left:0;top:2496px;width:1200px;height:559px;background:linear-gradient(90deg,#dfe3e6 0%,#ecedee 60%,#f0f1f2 100%)}

/* contact */
.contact-photo{position:absolute;left:573px;top:3166px;width:505px;height:342px;border-radius:0 90px 0 90px;background:linear-gradient(135deg,#8a6a4e 0%,#d6cbbb 40%,#3a4660 70%,#6b5640 100%)}
.contact-label{position:absolute;font-size:11px;font-weight:500;color:#666;letter-spacing:.3px}
.contact-value{position:absolute;font-size:16px;font-weight:600;color:var(--ink)}
.contact-value.small{font-size:14px}
.icon-dot{position:absolute;width:40px;height:40px;border-radius:50%;background:#7d7d7d}
.solid-btn{position:absolute;left:218px;top:3428px;width:152px;height:41px;border-radius:21px;background:var(--btn);color:var(--white);font-size:12px;font-weight:700;letter-spacing:1px;display:flex;align-items:center;justify-content:center}

/* footer */
.site-footer{position:absolute;left:0;top:3652px;width:1200px;height:413px;background:var(--footer);color:#e6e6e6}
.footer-brand{position:absolute;left:130px;top:124px;width:260px;text-align:center;font-size:21px;font-weight:500;letter-spacing:1px;color:var(--white);text-transform:uppercase}
.footer-about{position:absolute;left:141px;top:187px;width:245px;font-size:11px;line-height:20px;color:#cfcfcf}
.footer-divider{position:absolute;top:60px;width:1px;height:190px;background:var(--footer-line)}
.footer-head{position:absolute;top:108px;font-size:13px;font-weight:600;color:var(--white);letter-spacing:.4px}
.footer-links{position:absolute;top:138px;list-style:none;font-size:13px;line-height:25.5px;color:#cfcfcf}
.footer-links.small{font-size:11.5px}
.social{position:absolute;top:137px;width:30px;height:30px;border-radius:50%;background:var(--white)}
.footer-bottom{position:absolute;left:0;top:343px;width:1200px;height:1px;background:var(--footer-line)}
.copyright{position:absolute;top:364px;width:1200px;text-align:center;font-size:11px;color:#d0d0d0}
</style>
</head>
<body>

<header class="site-header">
  <div class="brand">Meridian Crest</div>
  <div class="call-btn">
    <svg width="16" height="16" viewBox="0 0 24 24" aria-hidden="true"><path fill="#fff" d="M6.6 10.8a15.1 15.1 0 0 0 6.6 6.6l2.2-2.2c.3-.3.7-.4 1-.2 1.1.4 2.3.6 3.6.6.6 0 1 .4 1 1V20c0 .6-.4 1-1 1C10.6 21 3 13.4 3 4c0-.6.4-1 1-1h3.5c.6 0 1 .4 1 1 0 1.3.2 2.5.6 3.6.1.3 0 .7-.2 1z"/></svg>
    CALL US (+123) 456 7890
  </div>
  <nav class="main-nav">
    <a class="active" style="left:357px">OUR COMPANY</a>
    <a style="left:491px">INVESTMENT APPRAOCH</a>
    <a style="left:687px">EXECUTIVE TEAM</a>
    <a style="left:838px">INVESTMENT PORTFOLIO</a>
    <a style="left:1036px">CONTACT</a>
  </nav>
  <div class="nav-underline"></div>
</header>

<section class="hero">
  <div class="hero-photo" role="img" aria-label="Aerial view of a city skyline with glass office towers"></div>
  <h1 class="hero-title">WELCOME TO <b>MERIDIAN CREST</b></h1>
  <div class="hero-sub">REAL ESTATE INVESTMENT FIRM</div>
  <a class="pill">LEARN MORE</a>
  <svg class="abs" style="left:0;top:600px" width="1200" height="90" viewBox="0 0 1200 90" aria-hidden="true">
    <polygon points="0,80 1200,10 1200,90 0,90" fill="#fff"/>
    <polygon points="632,50 1200,22 1200,92" fill="#bdbdbd"/>
    <line x1="599" y1="6" x2="599" y2="90" stroke="#9a9a9a" stroke-width="2"/>
  </svg>
</section>

<section>
  <div class="company-photo" role="img" aria-label="Modern glass office building against a blue sky"></div>
  <div class="eyebrow" style="left:625px;top:912px">Who we are</div>
  <h2 class="section-title" style="left:623px;top:933px">OUR <b>COMPANY</b></h2>
  <div class="rule" style="left:626px;top:981px;width:60px"></div>
  <div class="copy" style="left:626px;top:1004px;width:428px">
    <p>Lorem ipsum dolor sit amet, consectetur adipiscing elit, sed do eiusmod tempor incididunt ut labore et dolore magna aliqua.</p>
    <p>Ut enim ad minim veniam, quis nostrud exercitation ullamco laboris nisi ut aliquip ex ea commodo consequat. Duis aute irure dolor in reprehenderit in voluptate velit esse cillum dolore eu fugiat nulla pariatur. Excepteur sint occaecat cupidatasunt in culpa qui officia deserunt mollit anim id est laborum.</p>
  </div>
  <a class="outline-btn" style="left:624px;top:1200px;width:169px">LEARN MORE</a>
</section>

<section class="approach">
  <div class="eyebrow" style="left:0;top:61px;width:1200px;text-align:center;font-size:14px">What we do</div>
  <h2 class="section-title" style="left:0;top:83px;width:1200px;text-align:center;font-size:31px"><b>INVESTMENT</b> APPROACH</h2>
  <div class="rule" style="left:572px;top:128px;width:52px"></div>
</section>
<svg class="abs" style="left:1002px;top:1672px" width="76" height="112" aria-hidden="true"><polyline points="74,0 74,110 0,110" fill="none" stroke="#555" stroke-width="2"/></svg>
<article class="card" style="left:128px"><div class="photo" role="img" aria-label="Business handshake over documents" style="background:linear-gradient(160deg,#9a9a9a,#d8d2c6 50%,#7c6a55)"></div><h3>ACQUISITIONS</h3><p>Lorem ipsum dolor sit amet</p></article>
<article class="card" style="left:365px"><div class="photo" role="img" aria-label="Hands typing on a laptop with data overlays" style="background:linear-gradient(160deg,#27507a,#3f78a8 50%,#1e3450)"></div><h3>DUE DILIGENCE</h3><p>Lorem ipsum dolor sit amet</p></article>
<article class="card" style="left:602px"><div class="photo" role="img" aria-label="Rising financial growth chart in blue tones" style="background:linear-gradient(160deg,#5f8aa6,#2d5a78 50%,#173247)"></div><h3>FINANCING</h3><p>Lorem ipsum dolor sit amet</p></article>
<article class="card" style="left:838px"><div class="photo" role="img" aria-label="Presenter at a whiteboard in a meeting room" style="background:linear-gradient(160deg,#c9ccd0,#8d949b 50%,#4d5258)"></div><h3>MANAGEMENT</h3><p>Lorem ipsum dolor sit amet</p></article>

<section class="team">
  <div class="team-photo" role="img" aria-label="Two smiling business professionals standing back to back before a city skyline"></div>
  <div class="eyebrow" style="left:137px;top:135px">Who we are</div>
  <h2 class="section-title" style="left:135px;top:156px">MEET <b>THE TEAM</b></h2>
  <div class="copy" style="left:137px;top:227px;width:430px">
    <p>Lorem ipsum dolor sit amet, consectetur adipiscing elit, sed do eiusmod tempor incididunt ut labore et dolore magna aliqua.</p>
    <p>Ut enim ad minim veniam, quis nostrud exercitation ullamco laboris nisi ut aliquip ex ea commodo consequat. Duis aute irure dolor in reprehenderit in voluptate velit esse cillum dolo</p>
  </div>
  <a class="outline-btn" style="left:137px;top:381px;width:170px">LEARN MORE</a>
</section>
<svg class="abs" style="left:0;top:1866px" width="610" height="70" aria-hidden="true"><polygon points="0,2 602,30 0,68" fill="#a9a9a9"/></svg>

<section class="portfolio">
  <svg class="abs" style="left:0;top:0" width="700" height="559" aria-hidden="true">
    <defs><linearGradient id="sky" x1="0" y1="0" x2="1" y2="1"><stop offset="0" stop-color="#2c5d95"/><stop offset=".5" stop-color="#7fa9d4"/><stop offset="1" stop-color="#c9d9e6"/></linearGradient></defs>
    <polygon points="0,0 690,0 470,559 0,559" fill="url(#sky)" role="img" aria-label="Skyscrapers viewed from below against a cloudy sky"/>
  </svg>
  <div class="eyebrow" style="left:657px;top:156px;letter-spacing:.5px;font-size:15px">Our project gallery</div>
  <h2 class="section-title" style="left:656px;top:180px;font-size:35px"><b>INVESTMENT</b> PORTFOLIO</h2>
  <div class="rule dark" style="left:658px;top:229px;width:76px;height:3px"></div>
  <div class="copy" style="left:659px;top:252px;width:420px;text-align:left;line-height:25px;font-size:14px;hyphens:none">Lorem ipsum dolor sit amet, consectetur adipiscing elit, sed do eiusmod tempor incididunt ut labore et.<span style="font-size:12px">Ut enim ad minim veniam, quis nostrud exercitation ullamco laboris nisi ut aliquip ex ea commodo consequat. Duis aute irure</span></div>
  <a class="outline-btn" style="left:668px;top:379px;width:167px">LEARN MORE</a>
</section>

<section>
  <svg class="abs" style="left:153px;top:3132px" width="572" height="420" aria-hidden="true">
    <polyline points="569,34 569,2 2,2 2,416 569,416 569,378" fill="none" stroke="#d4d4d4" stroke-width="4"/>
  </svg>
  <div class="contact-photo" role="img" aria-label="Three colleagues reviewing documents around a laptop in an office"></div>
  <h2 class="section-title" style="left:220px;top:3190px;font-size:26px">CONTACT</h2>
  <h2 class="section-title" style="left:220px;top:3219px;font-size:26px"><b>MERIDIAN CREST</b></h2>
  <div class="rule dark" style="left:221px;top:3256px;width:58px;height:2px"></div>
  <div class="icon-dot" style="left:218px;top:3288px"></div>
  <svg class="abs" style="left:227px;top:3297px" width="22" height="22" viewBox="0 0 24 24" aria-hidden="true"><path fill="#fff" d="M6.6 10.8a15.1 15.1 0 0 0 6.6 6.6l2.2-2.2c.3-.3.7-.4 1-.2 1.1.4 2.3.6 3.6.6.6 0 1 .4 1 1V20c0 .6-.4 1-1 1C10.6 21 3 13.4 3 4c0-.6.4-1 1-1h3.5c.6 0 1 .4 1 1 0 1.3.2 2.5.6 3.6.1.3 0 .7-.2 1z"/></svg>
  <div class="contact-label" style="left:272px;top:3291px">PHONE NUMBER</div>
  <div class="contact-value" style="left:271px;top:3308px">(+123) 456 789</div>
  <div class="icon-dot" style="left:218px;top:3351px"></div>
  <svg class="abs" style="left:228px;top:3362px" width="20" height="18" viewBox="0 0 20 18" aria-hidden="true"><rect x="1" y="2" width="18" height="14" fill="none" stroke="#fff" stroke-width="2"/><polyline points="1,2 10,10 19,2" fill="none" stroke="#fff" stroke-width="2"/></svg>
  <div class="contact-label" style="left:272px;top:3356px">EMAIL ADDRESS</div>
  <div class="contact-value small" style="left:271px;top:3373px">info@companyname.com</div>
  <a class="solid-btn">CONTACT US</a>
</section>

<footer class="site-footer">
  <div class="footer-brand">Meridian Crest</div>
  <p class="footer-about">Lorem ipsum dolor sit amet, consectetur adipiscing elit, sed do eiusmod tempor incididunt ut labore et dolore</p>
  <div class="footer-divider" style="left:463px"></div>
  <div class="footer-divider" style="left:696px"></div>
  <div class="footer-divider" style="left:898px"></div>
  <div class="footer-head" style="left:499px">NAVIGATION</div>
  <ul class="footer-links" style="left:499px"><li>Our Company</li><li>Investment Approach</li><li>Team</li><li>Investment Portofolio</li></ul>
  <div class="footer-head" style="left:723px">LINKS</div>
  <ul class="footer-links small" style="left:725px"><li>Terms &amp; Condition</li><li>Privacy Policy</li><li>Contct Us</li></ul>
  <div class="footer-head" style="left:922px">FOLLOW US</div>
  <span class="social" style="left:921px"></span>
  <span class="social" style="left:956px"></span>
  <span class="social" style="left:991px"></span>
  <div class="footer-bottom"></div>
  <div class="copyright">© 2021 Meridian Crest &nbsp;|&nbsp; All Rights Reserved</div>
</footer>

</body>
</html>
```